Capacity building in Resource Management

Need design of a business card (later to be completed by letterhead and webdesign in same fashion) for a professional who works in the field of capacity building of professionals in mostly developing countries in the field waste/resource management, waste prevention/reduction, cleaner production, stakeholders involvement, etc.
Info on business cards is to include provided logo, info in provided file and picture.

Industry/Entity Type

Business

Contact Information for Business Card

White background

Font styles to use
Sans Serif

Colors

Designer to choose colors to be used in the design.

```html
<!DOCTYPE html>
<html lang="en">
<head>
<meta charset="utf-8">
<title>Terra-Learn Business Card</title>
<link href="https://fonts.googleapis.com/css2?family=Roboto:wght@400;500;700&family=Roboto+Condensed:wght@400;700&display=swap" rel="stylesheet">
<style>
  :root {
    --bg: #2b2b2b;
    --card: #f3f3f3;
    --green: #4f8a30;
    --green-dark: #3c5f22;
    --text: #555555;
    --muted: #7a7a7a;
    --white: #ffffff;
  }
  * { box-sizing: border-box; margin: 0; padding: 0; }
  html, body { width: 1200px; height: 960px; overflow: hidden; }
  body { background: var(--bg); font-family: "Roboto", Arial, sans-serif; position: relative; }

  .card {
    position: absolute; width: 600px; height: 343px;
    background: var(--card);
    box-shadow: 0 4px 10px rgba(0,0,0,.5);
    overflow: hidden;
  }
  .card--front { left: 314px; top: 113px; }
  .card--back { left: 311px; top: 472px; }

  .brand { position: absolute; display: flex; flex-direction: column; }
  .brand__row { display: flex; align-items: center; gap: 10px; }
  .brand__mark { width: 26px; height: 26px; background: var(--green); }
  .brand__name { font-weight: 700; color: var(--green); font-size: 36px; line-height: 1; }
  .brand__tagline { font-size: 10px; color: var(--text); margin-top: 6px; margin-left: 36px; }
  .card--front .brand { left: 45px; top: 52px; }
  .card--back .brand { left: 156px; top: 133px; }

  .address { position: absolute; left: 45px; top: 158px; font-size: 14px; line-height: 19px; color: var(--text); font-style: normal; }

  .contacts { position: absolute; left: 45px; top: 200px; list-style: none; }
  .contacts li { display: flex; align-items: center; height: 19px; font-size: 14px; color: var(--text); }
  .contacts .icon { width: 14px; height: 14px; margin-right: 11px; display: flex; align-items: center; justify-content: center; }
  .contacts .icon svg { width: 12px; height: 12px; }
  .icon__dot { width: 10px; height: 10px; background: var(--green); border-radius: 50%; }
  .icon__square { width: 10px; height: 10px; background: var(--green); }

  .portrait {
    position: absolute; left: 383px; top: 48px; width: 136px; height: 178px;
    border: 3px solid var(--white);
    box-shadow: 0 2px 5px rgba(0,0,0,.4);
    background: linear-gradient(160deg, #6f8a5e 0%, #9aa48c 45%, #d9d9d6 80%, #eeeeee 100%);
  }

  .title { position: absolute; left: 320px; width: 264px; top: 238px; text-align: center; text-transform: uppercase; }
  .title__name { font-family: "Roboto Condensed", Arial, sans-serif; font-size: 22px; font-weight: 700; color: var(--green); line-height: 26px; }
  .title__line { font-family: "Roboto", Arial, sans-serif; font-size: 15px; color: var(--muted); line-height: 19px; }

  .band { position: absolute; left: 0; bottom: 0; width: 600px; height: 29px; }
  .band__url { position: absolute; left: 45px; top: 6px; font-size: 14px; color: var(--white); letter-spacing: 2.4px; }

  .back-url { position: absolute; left: 0; width: 600px; top: 287px; text-align: center; font-size: 14px; letter-spacing: 5px; color: var(--text); }
</style>
</head>
<body>

<section class="card card--front">
  <div class="brand">
    <div class="brand__row">
      <span class="brand__mark"></span>
      <span class="brand__name">terra-learn</span>
    </div>
    <span class="brand__tagline">capacity building in resource management</span>
  </div>

  <address class="address">
    Lindenhof 12<br>10999 Berlin, Germany
  </address>

  <ul class="contacts">
    <li><span class="icon"><svg viewBox="0 0 24 24"><path fill="var(--green)" d="M6.6 10.8a15.1 15.1 0 0 0 6.6 6.6l2.2-2.2c.3-.3.7-.4 1-.2 1.1.4 2.3.6 3.6.6.6 0 1 .4 1 1V20c0 .6-.4 1-1 1A17 17 0 0 1 3 4c0-.6.4-1 1-1h3.5c.6 0 1 .4 1 1 0 1.2.2 2.4.6 3.6.1.3 0 .7-.2 1z"/></svg></span>+49 1500 000 1234 (also mobile)</li>
    <li><span class="icon"><svg viewBox="0 0 24 24"><rect x="2" y="5" width="20" height="14" fill="var(--green)"/><path d="M2 5l10 7 10-7" fill="none" stroke="var(--card)" stroke-width="2"/></svg></span>anna.weber@terra-learn.com</li>
    <li><span class="icon"><span class="icon__dot"></span></span>@annaweber</li>
    <li><span class="icon"><span class="icon__dot"></span></span>aweber2010</li>
    <li><span class="icon"><span class="icon__square"></span></span>Anna Weber</li>
  </ul>

  <div class="portrait" role="img" aria-label="Portrait photograph of the consultant"></div>

  <div class="title">
    <div class="title__name">Terra-Learn</div>
    <div class="title__line">Capacity building in</div>
    <div class="title__line">Resource management</div>
  </div>

  <div class="band">
    <svg width="600" height="29" viewBox="0 0 600 29">
      <rect x="0" y="0" width="600" height="29" fill="var(--green)"/>
      <polygon points="392,0 600,0 600,29 386,29" fill="var(--green-dark)"/>
      <polygon points="388,0 392,0 386,29 382,29" fill="var(--white)"/>
    </svg>
    <span class="band__url">www.terra-learn.com</span>
  </div>
</section>

<section class="card card--back">
  <div class="brand">
    <div class="brand__row">
      <span class="brand__mark"></span>
      <span class="brand__name">terra-learn</span>
    </div>
    <span class="brand__tagline">capacity building in resource management</span>
  </div>
  <div class="back-url">www.terra-learn.com</div>
</section>

</body>
</html>
```